Vorlen - Customer Experience Software Company Web Design

*****UPDATE*****
We've been getting a lot of corporate designs through. Unfortunately this is not what we are looking for. We would like our brand to be more approachable and for the look and feel to to be a bit more fun.
Also the best designs we have received so far have followed the "less is more" approach. Im hoping any news designs will take these aspects into account.
*****************

Background:

Vorlen is a Customer Experience Technology company. We equip business and technology teams with the frameworks, tools and services to help them create compelling experiences for their customers.

Our flagship product - Vorlen CX is an open-source customer experience application framework – it enables organisation to build highly differentiated business applications to deliver compelling experiences to your customers.

Vorlen CX is designed for innovators who understand that unlocking opportunity in today’s competitive marketplace is driven by delivering a better customer experience.

Task:

We are looking for a web design (we need PSD, no HTML/CSS) for our company site through which to launch our customer experience framework product. The site will be also used as a support site, so the functional aspect of the site is as important as the visual impact for sales.

In order to help us conceptualise ideas and content we have drafted a temporary website using a standard wordpress theme (please see details below). Now we have a general idea of our requirements we like we would like to take it to the next level and get some designs with that professional edge.

Our target market are Enterprise organisations - that is senior members of the business & technology teams (Business General Managers, CTO’s, CIO’s, and Senior Architects and Senior Developers). We want something clean & fresh which is DIFFERENT from the typical corporate technology websites out there. We would like to be seen as more approachable than most large technology companies.

Words we would like to use to describe the finished design:
• Clean (we’re thinking white background with one or two key colours)
• Fresh
• Light
• Modern
• Less is more
• Web 2.0
• Fun but professional (aimed at Enterprise/Large organisations)
• Bold, clear call to action – e.g. Live Demo & Download
• Readable (but Sans Serif)

As we’re a Customer Experience company, the usability of the site is critical. The site must be functional, intuitive & easy to navigate. We want to keep the number of user clicks to the bare minimum possible.

Other aspects, which we would like to incorporate into the site
• Home Page banner slider
• Client logon
• Newsletter sign up
• Social media links – Friendsy, Linkfold (for starters)
• Rich footer links

Some websites we like
• http://brightpanelworks.example - clean, light, modern & intuitive
• http://www.tamsoledrik.example - bold, clear messaging
• http://www.opengridhub.example/markup/emblem - punchy, colourful
• http://postwren.example/ - modern, clear messaging, colourful, rich footer area

Target Market(s)

Enterprise organisations - that is senior members of the business & technology teams (Business General Managers, CTO’s, CIO’s, Senior Devs)

Industry/Entity Type

Business

Requirements
Must have
• - Design Specs: Accepted file formats: During the design phase adobe PSD or JPEG are OK (if you need to upload files), but for the handover we'll need PSD only with all the original layers.
- The width needs to be a size that will work with every size computer screen
- Need to use cross-platform compatible font
- The graphic elements used for the design must be copyright free

Current test site
- URL http://vorlen.example/wp-admin
- username: artmarket
- password: artmarket

IMPORTANT NOTE REGARDING OUR CURRENT TEST SITE:

This is a very basic version of a site to help us generate requirements. This design is only a starting point/input and is not locked in stone i.e. we do not simply want this site simply tweaked around the edges.

We are looking for you to use all of your graphic design skills and experience to create a truly awesome site design!

```html
<!DOCTYPE html>
<html lang="en">
<head>
<meta charset="utf-8">
<title>Vorlen – Customer Experience Application Framework</title>
<link rel="stylesheet" href="https://fonts.googleapis.com/css2?family=Philosopher:wght@400;700&family=Arimo:wght@400;700&display=swap">
<style>
:root{
  --page:#c4c7d1;
  --page-light:#d3d6de;
  --page-dark:#b6b9c4;
  --ink:#151515;
  --ink-soft:#3b3d44;
  --muted:#8e919b;
  --nav-bg:#f3f3f4;
  --nav-edge:#a9acb5;
  --slider-dark:#1a1d2b;
  --slider-mid:#2c3146;
  --slider-bar:#c9d2e2;
  --dot:#1c1d22;
  --demo-red:#d8141a;
  --demo-red-dark:#a60a0e;
  --buy-blue:#2b7fd6;
  --buy-blue-dark:#175aa5;
  --footer:#bfc2cc;
  --divider:#9ea1ab;
  --white:#ffffff;
  --social-a:#1c7fc0;
  --social-b:#3d5b98;
}
*{box-sizing:border-box;margin:0;padding:0}
html,body{width:1098px;height:1200px;overflow:hidden}
body{
  position:relative;
  font-family:"Arimo",Arial,sans-serif;
  color:var(--ink);
  background:
    linear-gradient(180deg,#8a8d96 0,#8a8d96 3px,transparent 3px),
    linear-gradient(180deg,var(--page-light) 0,var(--page) 120px,var(--page) 900px,#e3e5ea 1000px,var(--page) 1030px,var(--footer) 1036px);
}
.abs{position:absolute}

/* header */
.brand{left:57px;top:36px;font-family:"Philosopher",sans-serif;font-weight:700;font-size:40px;color:var(--ink);letter-spacing:1px}
.main-nav{left:571px;top:31px;display:flex;gap:7px}
.main-nav a{
  display:block;height:25px;line-height:25px;padding:0 10px;min-width:61px;text-align:center;
  font-size:10px;font-weight:700;color:var(--ink);text-decoration:none;text-transform:uppercase;
  background:linear-gradient(180deg,#ffffff,#e2e3e6);border:1px solid var(--nav-edge);border-radius:6px;
  box-shadow:0 1px 2px rgba(0,0,0,.2);
}
.main-nav a.current{color:var(--muted);background:linear-gradient(180deg,#e6e7ea,#d4d6da)}
.account-links{left:952px;top:37px;display:flex;gap:18px}
.account-links a{font-size:10px;font-weight:700;color:var(--muted);text-decoration:none}
.tagline{left:153px;top:100px;width:300px;text-align:center;font-family:"Philosopher",sans-serif;font-size:25px;line-height:31px;color:var(--ink)}

/* slider */
.slider{left:165px;top:183px;width:768px;height:343px;border-top:2px solid #e8e9ee;box-shadow:0 2px 4px rgba(0,0,0,.15)}
.slide{width:768px;height:294px;background:radial-gradient(ellipse at 50% 85%,var(--slider-mid),var(--slider-dark) 70%)}
.slide-art{position:absolute;top:18px;height:260px;border-radius:6px}
.art-monitor{left:30px;width:210px;background:linear-gradient(160deg,#b7bfcf 0,#6a4c8e 30%,#2a2c3e 70%,transparent)}
.art-bars{left:310px;width:170px;background:linear-gradient(90deg,#e5352f 0,#f1c21a 35%,#7ccf3d 65%,#2aa4e0 100%);opacity:.75;top:60px;height:200px}
.art-pie{left:525px;width:210px;top:70px;height:180px;border-radius:50%;background:conic-gradient(#6ccd32 0 25%,#f0b425 25% 50%,#e43a2c 50% 75%,#8b3fc4 75% 88%,#3a5cd6 88%)}
.slider-bar{height:47px;background:linear-gradient(180deg,#dde3ee,var(--slider-bar));border-top:1px solid #eef1f6}
.dots{position:absolute;right:53px;bottom:17px;display:flex;gap:8px}
.dots span{width:9px;height:9px;border-radius:50%;background:var(--dot)}
.dots span:first-child{background:#6b6e78}

/* calls to action */
.cta{left:165px;top:593px;display:flex;gap:7px}
.cta a{display:block;height:39px;line-height:39px;text-align:center;font-family:"Philosopher",sans-serif;font-size:24px;color:var(--white);text-decoration:none;border-radius:3px;text-transform:uppercase}
.btn-demo{width:138px;background:linear-gradient(180deg,var(--demo-red),var(--demo-red-dark));color:var(--ink)!important}
.btn-buy{width:69px;background:linear-gradient(180deg,var(--buy-blue),var(--buy-blue-dark))}
.trial{left:165px;top:646px;width:214px;text-align:center;font-family:"Philosopher",sans-serif;font-size:15px;line-height:19px;font-variant:small-caps;color:var(--ink)}
.trial a{color:var(--ink)}
.rule{left:397px;top:700px;width:1px;height:250px;background:linear-gradient(180deg,transparent,var(--divider) 20%,var(--divider) 80%,transparent)}

/* content */
.content{left:420px;top:585px;width:514px}
.content h1{font-family:"Philosopher",sans-serif;font-weight:400;font-size:28px;line-height:36px}
.content h2{font-family:"Philosopher",sans-serif;font-weight:400;font-size:20px;line-height:26px;margin-top:14px}
.content p{font-size:9.5px;line-height:12.3px;color:var(--ink-soft);margin-top:16px;text-align:justify}
.content h1 + p{margin-top:20px}

/* footer */
.footer{left:0;top:1036px;width:1098px;height:164px;border-top:1px solid #8f929c}
.footer-col{position:absolute;top:17px}
.footer-col h3{font-weight:400;font-size:20px;line-height:24px;color:var(--ink)}
.footer-col ul{list-style:none;margin-top:10px}
.footer-col li{font-size:11.5px;line-height:14.6px}
.footer-col a{color:var(--ink);text-decoration:none}
.col-company{left:42px}
.col-start{left:202px}
.col-support{left:427px}
.footer-divider{left:549px;top:4px;width:1px;height:160px;background:var(--divider)}
.newsletter{left:591px;top:17px}
.newsletter h3{font-weight:400;font-size:20px;line-height:24px}
.newsletter .field{display:block;margin-top:6px;width:236px;height:21px;background:var(--white);border:1px solid #a6a9b2;font-size:10px;line-height:19px;padding-left:12px;color:var(--ink)}
.newsletter .submit{display:block;margin-top:4px;width:72px;height:27px;line-height:25px;text-align:center;font-size:10px;color:var(--ink-soft);background:linear-gradient(180deg,#fbfbfc,#dcdde1);border:1px solid var(--nav-edge);border-radius:7px}
.follow{left:969px;top:17px}
.follow h3{font-weight:400;font-size:20px;line-height:24px}
.social{list-style:none;margin-top:6px}
.social li{display:flex;align-items:center;gap:6px;font-size:11.5px;line-height:14px;margin-bottom:5px}
.social a{color:var(--ink);text-decoration:none}
.social .sq{width:13px;height:13px;border-radius:2px}
.sq-a{background:var(--social-a)}
.sq-b{background:var(--social-b)}
</style>
</head>
<body>

<header>
  <div class="brand abs">Vorlen</div>
  <nav class="main-nav abs">
    <a class="current" href="#">Home</a>
    <a href="#">Products</a>
    <a href="#">Support</a>
    <a href="#">Blog</a>
    <a href="#">About</a>
  </nav>
  <div class="account-links abs"><a href="#">SIGN UP</a><a href="#">LOG IN</a></div>
  <p class="tagline abs">The customer experience application framework</p>
</header>

<section class="slider abs">
  <div class="slide" style="position:relative">
    <div class="slide-art art-monitor" role="img" aria-label="Desktop monitor showing a purple wallpaper"></div>
    <div class="slide-art art-bars" role="img" aria-label="Colourful 3D bar chart illustration"></div>
    <div class="slide-art art-pie" role="img" aria-label="Colourful 3D pie chart illustration"></div>
  </div>
  <div class="slider-bar">
    <div class="dots"><span></span><span></span><span></span><span></span><span></span><span></span><span></span><span></span><span></span></div>
  </div>
</section>

<div class="cta abs">
  <a class="btn-demo" href="#">Live Demo</a>
  <a class="btn-buy" href="#">Buy</a>
</div>
<p class="trial abs">30-day <a href="#"><b>Free</b></a> trial for Panes OS<br>Also available <a href="#">for Orchard OS</a></p>
<div class="rule abs"></div>

<main class="content abs">
  <h1>Creat compelling experiences for your customers</h1>
  <p>Lorem ipsum dolor sit amet, consec tetuer adipiscing elit. Praesent vestibulum molestie lacus. Aenean nonummy hen drerit mauris. Phasellus porta. Fusce suscipit varius mi. Cum sociis natoque read our.Lorem ipsum dolor sit amet, consec tetuer adipiscing elit. Praesent vestibulum molestie lacus. Aenean nonummy hen drerit mauris. Phasellus porta. Fusce suscipit varius mi. Cum sociis natoque read our.Lorem ipsum dolor sit amet, consec tetuer adipiscing elit. Praesent vestibulum molestie lacus. Aenean nonummy hen drerit mauris. Phasellus porta. Fusce suscipit varius mi. Cum sociis natoque read our.</p>
  <h2>Opportunity through customer experience innovation</h2>
  <p>Lorem ipsum dolor sit amet, consec tetuer adipiscing elit. Praesent vestibulum molestie lacus. Aenean nonummy hen drerit mauris. Phasellus porta. Fusce suscipit varius mi. Cum sociis natoque read our.Lorem ipsum dolor sit amet, consec tetuer adipiscing elit. Praesent vestibulum molestie lacus. Aenean nonummy hen drerit mauris. Phasellus porta. Fusce suscipit varius mi. Cum sociis natoque read our.Lorem ipsum dolor sit amet, consec tetuer adipiscing elit. Praesent vestibulum molestie lacus. Aenean nonummy hen drerit mauris. Phasellus porta. Fusce suscipit varius mi. Cum sociis natoque read our.</p>
  <h2>True difference</h2>
  <p>Lorem ipsum dolor sit amet, consec tetuer adipiscing elit. Praesent vestibulum molestie lacus. Aenean nonummy hen drerit mauris. Phasellus porta. Fusce suscipit varius mi. Cum sociis natoque read our.Lorem ipsum dolor sit amet, consec tetuer adipiscing elit. Praesent vestibulum molestie lacus. Aenean nonummy hen drerit mauris. Phasellus porta. Fusce suscipit varius mi. Cum sociis natoque read our.Lorem ipsum dolor sit amet, consec tetuer adipiscing elit. Praesent vestibulum molestie lacus. Aenean nonummy hen drerit mauris. Phasellus porta. Fusce suscipit varius mi. Cum sociis natoque read our.</p>
</main>

<footer class="footer abs">
  <div class="footer-col col-company">
    <h3>Vorlen</h3>
    <ul><li><a href="#">Home</a></li><li><a href="#">Products</a></li><li><a href="#">Support</a></li><li><a href="#">Blog</a></li><li><a href="#">About</a></li></ul>
  </div>
  <div class="footer-col col-start">
    <h3>Getting Started</h3>
    <ul><li><a href="#">Demo</a></li><li><a href="#">Documentation</a></li><li><a href="#">Download</a></li></ul>
  </div>
  <div class="footer-col col-support">
    <h3>Support</h3>
    <ul><li><a href="#">Contact Us</a></li><li><a href="#">Vorlen Services</a></li><li><a href="#">Vorlen Support</a></li></ul>
  </div>
  <div class="footer-divider abs"></div>
  <div class="newsletter abs">
    <h3>Subscribe to our newsletter</h3>
    <span class="field">Email Address</span>
    <span class="submit">Subscribe</span>
  </div>
  <div class="follow abs">
    <h3>Follow Us</h3>
    <ul class="social">
      <li><span class="sq sq-a"></span><a href="#">Linkfold</a></li>
      <li><span class="sq sq-b"></span><a href="#">Friendsy</a></li>
    </ul>
  </div>
</footer>

</body>
</html>
```